Web Design for ORV Air conditioning company

Hello,

I am calling on you for the modernization of the company's website
https://clim-solaris-atelier.fr/

The new one must include the new logo with the new graphic charter (color, style ...)

I'm looking for a simple design (less is more), a font written without Serif, the logo that brings a touch of color and modernity.

(maintenance and installation company for air conditioning and ventilation systems)
COLORS: in line with the logo

CHAPTER:

# PRESENTATION
# SERVICES
AIR CONDITIONING (ice cube icon)
HEATING (flame icon)
AIR TREATMENT (icon fan)
# ACHIEVEMENTS

# CONTACT
CONTACT FORM
GOOGLE MAPS

Target Market(s)

Showcase site for our customers

Coding

Coded - Design and coding required

Number of Pages Required

4 page

Font styles to use
Sans Serif

Colors
33b8a4
33a6d7
3176b5
ffffff

Requirements
Must have
• Clear and fluid navigation
a visual identity of the page with the logo
Should not have
• Overloaded.

```html
<!DOCTYPE html>
<html lang="en">
<head>
<meta charset="utf-8">
<title>ORV – Air Conditioning &amp; Maintenance</title>
<link href="https://fonts.googleapis.com/css2?family=Poppins:wght@300;400;500;600&display=swap" rel="stylesheet">
<style>
:root{
  --blue:#2a8cc4;
  --teal:#33b8a4;
  --sky:#33a6d7;
  --navy:#3176b5;
  --dark:#1e1e1e;
  --text:#333;
  --muted:#666;
  --panel:#f4f4f4;
  --ink:#2b3440;
  --white:#fff;
}
*{box-sizing:border-box;margin:0;padding:0}
html,body{width:1200px;height:2618px;overflow:hidden}
body{font-family:'Poppins',sans-serif;color:var(--text);background:var(--white);position:relative}
.abs{position:absolute}
.btn{position:absolute;display:flex;align-items:center;justify-content:center;background:var(--blue);color:var(--white);font-size:11.5px;font-weight:500;border-radius:2px}
.btn.outline{background:var(--white);color:var(--blue);border:1.5px solid var(--blue)}
.mark{display:block}
h2{font-size:22px;font-weight:600;color:var(--dark);letter-spacing:.2px}

/* header */
.logo{left:182px;top:14px;display:flex;align-items:flex-end;gap:10px}
.logo-name{font-size:40px;font-weight:600;color:var(--teal);line-height:1}
.logo-tag{font-size:11px;font-weight:500;color:#7a8a96;padding-bottom:4px}
.follow{left:727px;top:29px;font-size:11px;display:flex;align-items:center;gap:6px}
.dot{width:17px;height:17px;border-radius:50%;background:var(--sky);display:inline-block}
.phone{left:898px;top:24px;display:flex;align-items:center;gap:8px;font-size:14px;font-weight:600;color:var(--dark)}
.nav{left:182px;top:67px;width:836px;border-top:1px solid #e4e4e4;padding-top:3px;height:32px;display:flex;align-items:center}
.nav a{font-size:11px;color:var(--dark);text-decoration:none;height:28px;display:flex;align-items:center;padding:0 21px}
.nav a.active{background:var(--blue);color:var(--white);width:74px;justify-content:center;padding:0}
.inquire{left:894px;top:71px;width:124px;height:27px;background:var(--ink);color:var(--white);font-size:11px;display:flex;align-items:center;justify-content:center}

/* hero */
.hero{left:0;top:102px;width:1200px;height:458px;background:linear-gradient(110deg,#8a8f96 0%,#b9bcc0 40%,#9a9fa5 70%,#7d8287 100%)}
.hero-shade{position:absolute;inset:0;background:rgba(0,0,0,.25)}
.hero h1{position:absolute;top:152px;width:100%;text-align:center;font-size:38px;line-height:42px;font-weight:600;color:var(--white)}
.hero p{position:absolute;top:248px;width:100%;text-align:center;font-size:12px;color:var(--white)}

/* services */
.center-title{width:1200px;text-align:center}
.card{top:681px;width:266px}
.card .pic{height:194px}
.card .icon{position:absolute;left:97px;top:155px;width:72px;height:72px;background:var(--white);border-radius:4px;box-shadow:0 2px 6px rgba(0,0,0,.12);display:flex;align-items:center;justify-content:center}
.card h3{position:absolute;top:228px;width:100%;text-align:center;font-size:17px;font-weight:500;color:var(--dark)}
.card p{position:absolute;top:255px;left:20px;right:20px;text-align:center;font-size:10.5px;line-height:16px;color:var(--muted)}

/* achievements */
.ach{left:0;top:1075px;width:681px;height:411px;background:var(--panel)}
.ach-pic{left:681px;top:1075px;width:519px;height:411px;background:radial-gradient(circle at 50% 45%,#6d89c6 0%,#3d5ea3 55%,#1e3d7c 100%)}
.lead{font-size:15px;font-weight:600;color:var(--dark);line-height:21px}
.body{font-size:11.2px;line-height:17.5px;color:var(--text)}

/* who */
.who-pic{left:213px;top:1547px;width:325px;height:401px;background:linear-gradient(160deg,#d7dce3 0%,#b5bfcc 45%,#2d3e62 100%)}
.stats{left:591px;top:1814px;width:420px;display:flex;justify-content:space-between;text-align:center}
.stats b{display:block;font-size:22px;font-weight:500;color:var(--blue);line-height:26px}
.stats span{font-size:12.5px;color:var(--text)}

/* inquiry */
.inq{left:0;top:2012px;width:1200px;height:462px;background:var(--panel)}
.field{position:absolute;left:182px;width:337px;height:33px;background:var(--white);border:1px solid #e6e6e6;font-size:10.5px;color:#888;padding:10px 9px}
.accent{left:827px;top:2045px;width:191px;height:275px;background:linear-gradient(135deg,#45d18a 0%,var(--teal) 40%,#2a9bbd 100%)}
.map{left:565px;top:2073px;width:427px;height:305px;background:linear-gradient(135deg,#e8ece8 0%,#eef0ec 50%,#e3e8e4 100%);border:2px solid var(--white)}

/* footer */
.foot{left:0;top:2474px;width:1200px;height:144px;background:var(--blue)}
.info{left:231px;top:2427px;width:739px;height:92px;background:var(--white);box-shadow:0 2px 10px rgba(0,0,0,.08);display:flex;align-items:center;justify-content:space-around;padding:0 30px}
.info-item{display:flex;align-items:center;gap:12px;font-size:10px;line-height:13.5px;color:var(--dark)}
.info-item strong{font-weight:600;display:block}
.foot-nav{left:0;top:2538px;width:1200px;display:flex;justify-content:center;gap:28px;font-size:11px;color:var(--white)}
.copy{left:225px;top:2589px;font-size:10.5px;color:var(--white)}
.foot-social{left:896px;top:2584px;display:flex;gap:11px}
.foot-social .dot{background:var(--white);width:18px;height:18px}
</style>
</head>
<body>

<!-- header -->
<header>
  <div class="abs logo"><span class="logo-name">ORV</span><span class="logo-tag">ORVANE MAINTENANCE INDUSTRIE</span></div>
  <div class="abs follow">Follow Us <span class="dot"></span><span class="dot"></span><span class="dot"></span><span class="dot"></span></div>
  <div class="abs phone">
    <svg width="20" height="20" viewBox="0 0 24 24" fill="none" stroke="var(--blue)" stroke-width="1.6"><path d="M5 3h4l2 5-2.5 1.5a11 11 0 0 0 6 6L16 13l5 2v4a2 2 0 0 1-2 2A16 16 0 0 1 3 5a2 2 0 0 1 2-2z"/></svg>
    04 71 22 39 50
  </div>
  <nav class="abs nav">
    <a class="active">Home</a><a>Presentation</a><a>Our Services</a><a>Achievements</a><a>Who are we?</a><a>Contact Us</a>
  </nav>
  <div class="abs inquire">INQUIRE NOW</div>
</header>

<!-- hero -->
<section class="abs hero" role="img" aria-label="Technician servicing a wall-mounted air conditioning unit">
  <div class="hero-shade"></div>
  <h1>Orvane Maintenance<br>Industrie Grenoble</h1>
  <p>LA SOLUTION A VOTRE PROBLÈME DE MAINTENANCE</p>
  <div class="btn" style="left:552px;top:290px;width:96px;height:30px;font-size:12px">Read More</div>
</section>

<!-- services -->
<section>
  <h2 class="abs center-title" style="top:610px;font-size:23px">OUR SERVICES</h2>
  <svg class="abs" style="left:583px;top:640px" width="34" height="9" viewBox="0 0 34 9"><path d="M0 2h12M22 2h12" stroke="var(--teal)" stroke-width="2.5"/><path d="M13 2l4 4 4-4" stroke="var(--blue)" stroke-width="2.5" fill="none"/></svg>

  <div class="abs card" style="left:182px">
    <div class="pic" role="img" aria-label="Outdoor air conditioning unit being installed" style="background:linear-gradient(135deg,#c9d3e6,#8ea3c7 60%,#5d6f96)"></div>
    <div class="icon"><svg width="46" height="46" viewBox="0 0 46 46" fill="none" stroke="var(--sky)" stroke-width="2"><path d="M23 4l9 5v10l-9 5-9-5V9z"/><path d="M12 21l9 5v10l-9 5-9-5V26z"/><path d="M34 21l9 5v10l-9 5-9-5V26z"/></svg></div>
    <h3>Air Conditioning</h3>
    <p>Lorem Ipsum is simply dummy text of the printing and typesetting industry...</p>
    <div class="btn outline" style="left:88px;top:303px;width:90px;height:27px">Read More</div>
  </div>

  <div class="abs card" style="left:467px">
    <div class="pic" role="img" aria-label="Radiator with thermostatic valve" style="background:linear-gradient(135deg,#e4e7ec,#aeb6c2 60%,#6d7684)"></div>
    <div class="icon"><svg width="40" height="46" viewBox="0 0 40 46"><path d="M20 2c3 10 16 15 16 28a16 16 0 0 1-32 0c0-8 5-12 7-17 1 5 3 7 5 8 0-7 2-13 4-19z" fill="var(--sky)"/><path d="M20 25c3 4 7 6 7 11a7 7 0 0 1-14 0c0-4 4-7 7-11z" fill="var(--white)"/></svg></div>
    <h3>Heating</h3>
    <p>Lorem Ipsum is simply dummy text of the printing and typesetting industry...</p>
    <div class="btn" style="left:88px;top:303px;width:90px;height:27px">Read More</div>
  </div>

  <div class="abs card" style="left:752px">
    <div class="pic" role="img" aria-label="Close-up of an industrial ventilation fan" style="background:radial-gradient(circle at 50% 45%,#d8f0ff,#4aa7db 45%,#1b4f86)"></div>
    <div class="icon"><svg width="44" height="44" viewBox="0 0 44 44" fill="var(--sky)"><circle cx="22" cy="22" r="4"/><path d="M22 18c-6-2-6-12 2-13 6 0 6 8 0 11z"/><path d="M26 22c2-6 12-6 13 2 0 6-8 6-11 0z"/><path d="M22 26c6 2 6 12-2 13-6 0-6-8 0-11z"/><path d="M18 22c-2 6-12 6-13-2 0-6 8-6 11 0z"/></svg></div>
    <h3>Air Treatment</h3>
    <p>Lorem Ipsum is simply dummy text of the printing and typesetting industry...</p>
    <div class="btn" style="left:88px;top:303px;width:90px;height:27px">Read More</div>
  </div>
</section>

<!-- achievements -->
<section>
  <div class="abs ach"></div>
  <div class="abs ach-pic" role="img" aria-label="Silver star trophy on a blue background"></div>
  <h2 class="abs" style="left:219px;top:1127px">ACHIEVEMENTS</h2>
  <svg class="abs" style="left:290px;top:1156px" width="34" height="9" viewBox="0 0 34 9"><path d="M0 2h12M22 2h12" stroke="var(--teal)" stroke-width="2.5"/><path d="M13 2l4 4 4-4" stroke="var(--blue)" stroke-width="2.5" fill="none"/></svg>
  <p class="abs lead" style="left:219px;top:1193px;width:420px">Lorem Ipsum is simply dummy text of the printing and typesetting industry.</p>
  <p class="abs body" style="left:219px;top:1258px;width:420px">Lorem Ipsum has been the industry's standard dummy text ever since the 1500s, when an unknown printer took a galley of type and scrambled it to make a type specimen book.</p>
  <p class="abs body" style="left:219px;top:1334px;width:420px">It has survived not only five centuries, but also the leap into electronic typesetting, remaining essentially unchanged.</p>
  <div class="btn" style="left:219px;top:1405px;width:90px;height:27px">Read More</div>
</section>

<!-- who are we -->
<section>
  <div class="abs who-pic" role="img" aria-label="Engineer in a blue hard hat with arms crossed"></div>
  <h2 class="abs" style="left:591px;top:1574px">WHO ARE WE?</h2>
  <svg class="abs" style="left:656px;top:1603px" width="34" height="9" viewBox="0 0 34 9"><path d="M0 2h12M22 2h12" stroke="var(--teal)" stroke-width="2.5"/><path d="M13 2l4 4 4-4" stroke="var(--blue)" stroke-width="2.5" fill="none"/></svg>
  <p class="abs lead" style="left:591px;top:1639px;width:400px">Lorem Ipsum is simply dummy text of the printing and typesetting industry.</p>
  <p class="abs body" style="left:591px;top:1704px;width:420px">Lorem Ipsum has been the industry's standard dummy text ever since the 1500s, when an unknown printer took a make a type specimen book.</p>
  <p class="abs body" style="left:591px;top:1763px;width:420px">It has survived not only five centuries, but also the leap into electronic typesetting, remaining essentially unchanged.</p>
  <div class="abs stats">
    <div><b>7</b><span>Clients</span></div>
    <div><b>650</b><span>Contract</span></div>
    <div><b>590</b><span>Satisfied</span></div>
    <div><b>1752</b><span>Stock Products</span></div>
  </div>
  <div class="btn" style="left:591px;top:1890px;width:96px;height:29px;font-size:12px">Read More</div>
</section>

<!-- quick inquiry -->
<section>
  <div class="abs inq"></div>
  <h2 class="abs" style="left:182px;top:2067px;font-size:18px">QUICK INQUIRY</h2>
  <svg class="abs" style="left:243px;top:2091px" width="34" height="9" viewBox="0 0 34 9"><path d="M0 2h12M22 2h12" stroke="var(--teal)" stroke-width="2.5"/><path d="M13 2l4 4 4-4" stroke="var(--blue)" stroke-width="2.5" fill="none"/></svg>
  <div class="field" style="top:2124px">Name</div>
  <div class="field" style="top:2167px">Email</div>
  <div class="field" style="top:2210px">Phone</div>
  <div class="field" style="top:2253px;height:83px">Message</div>
  <div class="btn" style="left:182px;top:2349px;width:337px;height:29px;font-size:11.5px">Submit</div>
  <div class="abs accent"></div>
  <div class="abs map" role="img" aria-label="Street map showing the company location"></div>
</section>

<!-- footer -->
<footer>
  <div class="abs foot"></div>
  <div class="abs info">
    <div class="info-item">
      <svg width="18" height="24" viewBox="0 0 18 24"><path d="M9 1a8 8 0 0 0-8 8c0 6 8 14 8 14s8-8 8-14a8 8 0 0 0-8-8z" fill="var(--blue)"/><circle cx="9" cy="9" r="3" fill="var(--white)"/></svg>
      <div><strong>Location</strong>14 Allée des Tilleuls<br>38320 EYBENS</div>
    </div>
    <div class="info-item">
      <svg width="22" height="16" viewBox="0 0 22 16" fill="none" stroke="var(--blue)" stroke-width="1.8"><rect x="1" y="1" width="20" height="14"/><path d="M1 1l10 8 10-8M1 15l7-7M21 15l-7-7"/></svg>
      <div><strong>Email</strong>contact@orv-maintenance.fr</div>
    </div>
    <div class="info-item">
      <svg width="20" height="20" viewBox="0 0 24 24"><path d="M5 3h4l2 5-2.5 1.5a11 11 0 0 0 6 6L16 13l5 2v4a2 2 0 0 1-2 2A16 16 0 0 1 3 5a2 2 0 0 1 2-2z" fill="var(--blue)"/></svg>
      <div><strong>Call Us &amp; Fax</strong><b>C:</b> 04 71 22 39 50<br><b>F:</b> 04 71 22 39 58</div>
    </div>
  </div>
  <div class="abs foot-nav"><span>Home</span><span>Presentation</span><span>Our Services</span><span>Achievements</span><span>Who are we?</span><span>Contact Us</span></div>
  <div class="abs copy">Copyright © 2020 ORV. All Rights Reserved</div>
  <div class="abs foot-social"><span class="dot"></span><span class="dot"></span><span class="dot"></span><span class="dot"></span></div>
</footer>

</body>
</html>
```